Mr Pellowes Yard Works flyer for newsletter

I need a professional looking flyer design for my company Mr Pellowes Yard Works based in New Braunfels, TX to boost sales. Must include the following: Lawn service starting at $40 (mowing, edging, leaf blowing) Tree trimming starting at $125. Other services-mulching, shrub trimming, aeration, flower bed maintenance, Fall/spring clean up. Serving New Braunfels and surrounding areas. To set up and estimate please call 512 555 0143 or email mrpellowesyard@example-mail.net

Industry/Entity Type

Landscaping

Font styles to use
Serif

Colors

Designer to choose colors to be used in the design.

Requirements
Must have
• Phone number 512 555 0143
• Email mrpellowesyard@example-mail.net

```html
<!DOCTYPE html>
<html lang="en">
<head>
<meta charset="utf-8">
<title>Mr Pellowes Yard Works – Flyer</title>
<link rel="stylesheet" href="https://fonts.googleapis.com/css2?family=Nunito:wght@400;700;800;900&family=Oswald:wght@500;600&family=Poppins:wght@300;700;800&display=swap">
<style>
  :root {
    --backdrop: #3a3a3a;
    --cream: #f7f6e9;
    --grass: #3c9c1f;
    --grass-dark: #0b5b23;
    --panel-green: #0d8c30;
    --lime: #8cc63f;
    --lime-text: #a8d42f;
    --yellow: #f6e61a;
    --red: #c8102e;
    --orange: #d35a1c;
    --ink: #111111;
    --white: #ffffff;
  }
  * { margin: 0; padding: 0; box-sizing: border-box; }
  html, body { width: 895px; height: 1200px; overflow: hidden; background: var(--backdrop); }
  body { position: relative; font-family: "Nunito", sans-serif; }

  .flyer {
    position: absolute; left: 80px; top: 83px; width: 735px; height: 1044px;
    background: var(--cream); overflow: hidden;
  }
  .abs { position: absolute; }

  .hero-photo {
    left: 0; top: 0; width: 735px; height: 252px;
    background: linear-gradient(180deg, #a9c7de 0%, #c9b79a 28%, #6f8d4a 45%, #5fb52c 70%, #4fa624 100%);
  }
  .mower-photo {
    left: 78px; top: 266px; width: 262px; height: 186px;
    border-radius: 12px;
    background: linear-gradient(135deg, #2a2a2a 0%, #3a3a3a 35%, #b3172a 60%, #c8192a 100%);
  }

  .brand-tag {
    left: 422px; top: 235px; width: 267px; height: 42px;
    background: var(--red); color: var(--white);
    font-family: "Poppins", sans-serif; font-weight: 300; font-size: 29px;
    line-height: 42px; text-align: center; letter-spacing: 0.5px;
  }
  .title-word {
    font-family: "Poppins", sans-serif; font-weight: 800; color: var(--grass);
    letter-spacing: -3px; line-height: 1;
  }
  .title-yard { left: 340px; top: 283px; font-size: 110px; }
  .title-works { left: 340px; top: 398px; font-size: 100px; }
  .location {
    left: 496px; top: 384px; font-family: "Oswald", sans-serif; font-weight: 500;
    font-size: 17px; color: var(--orange); letter-spacing: 0.2px;
  }

  .service-tiles { left: 15px; top: 452px; }

  .offer-panel {
    left: 391px; top: 517px; width: 305px; height: 375px;
    background: var(--panel-green); border-radius: 14px; color: var(--white);
    padding: 24px 0 0 27px;
  }
  .offer-heading { font-weight: 700; font-size: 29px; line-height: 34px; }
  .offer-heading .accent { color: var(--yellow); }
  .offer-rule { width: 222px; height: 9px; background: var(--lime); margin: 18px 0 14px; }
  .offer-label { font-weight: 800; font-size: 20px; color: var(--lime-text); letter-spacing: 0.3px; }
  .offer-list { list-style: none; margin-top: 3px; }
  .offer-list li {
    display: flex; align-items: center; gap: 6px;
    font-weight: 700; font-size: 16.5px; line-height: 26px; letter-spacing: 0.3px;
  }
  .offer-list svg { width: 14px; height: 14px; flex: none; }

  .price-lawn {
    left: 96px; top: 766px; width: 225px; height: 80px;
    background: var(--red); border-radius: 14px; color: var(--white);
    text-align: center; padding-top: 5px;
  }
  .price-lawn .price-main { font-weight: 800; font-size: 22px; line-height: 25px; }
  .price-lawn .price-fig { color: var(--yellow); }
  .price-lawn .price-note { font-weight: 400; font-size: 13px; line-height: 18px; }
  .price-tree {
    left: 96px; top: 857px; width: 225px; text-align: center;
    font-weight: 800; font-size: 22px; line-height: 26px; color: #5cb52d;
  }
  .price-tree .price-fig { color: var(--red); }

  .footer-band { left: 0; top: 937px; width: 735px; height: 107px; background: var(--grass-dark); }
  .coverage-pill {
    left: 85px; top: 921px; height: 41px; display: flex;
    font-family: "Oswald", sans-serif; font-weight: 500; font-size: 17px; line-height: 41px;
  }
  .coverage-area { width: 380px; background: var(--yellow); color: var(--grass-dark); border-radius: 20px 0 0 20px; text-align: center; }
  .coverage-type { width: 238px; background: var(--ink); color: var(--white); border-radius: 0 20px 20px 0; text-align: center; }

  .cta-label {
    left: 60px; top: 990px; font-weight: 900; font-size: 19px; color: var(--lime-text); letter-spacing: 0.3px;
  }
  .cta-phone {
    left: 362px; top: 969px; font-family: "Poppins", sans-serif; font-weight: 700;
    font-size: 33px; color: var(--white); letter-spacing: 0.5px; line-height: 44px;
  }
  .cta-email {
    left: 368px; top: 1010px; font-weight: 800; font-size: 14.5px; color: var(--white);
  }
  .cta-email .email-address { color: var(--lime-text); }
</style>
</head>
<body>
  <main class="flyer">
    <div class="abs hero-photo" role="img" aria-label="Photo of a tidy suburban house with a freshly mown front lawn and flower beds"></div>
    <div class="abs mower-photo" role="img" aria-label="Photo of a red and black push lawn mower"></div>

    <div class="abs brand-tag">MR PELLOWES</div>
    <div class="abs title-word title-yard">Yard</div>
    <div class="abs location">BASED IN NEW BRAUNFELS, TX</div>
    <div class="abs title-word title-works">Works</div>

    <svg class="abs service-tiles" width="350" height="300" viewBox="0 0 350 300">
      <g stroke="#ffffff" stroke-width="10" stroke-linejoin="round">
        <polygon points="125,8 345,8 330,130 95,130" fill="#5d8f3a" role="img" aria-label="Photo of a garden bed with a wheelbarrow and shovel"/>
        <polygon points="30,72 255,72 235,205 10,205" fill="#7c9a52" role="img" aria-label="Photo of a hedge being cut with a trimmer"/>
        <polygon points="100,158 340,158 320,290 80,290" fill="#4f7d35" role="img" aria-label="Photo of hands pruning a flowering plant"/>
      </g>
    </svg>

    <section class="abs offer-panel">
      <h2 class="offer-heading">Cater to all<br>your <span class="accent">Lawn Care</span><br>&amp; Gardening<br>Services</h2>
      <div class="offer-rule"></div>
      <h3 class="offer-label">OUR SERVICES</h3>
      <ul class="offer-list">
        <li><svg viewBox="0 0 14 14"><path d="M2 12 C2 5 6 2 13 2 C13 9 9 12 2 12 Z" fill="#a8d42f"/></svg>MULCHING</li>
        <li><svg viewBox="0 0 14 14"><path d="M2 12 C2 5 6 2 13 2 C13 9 9 12 2 12 Z" fill="#a8d42f"/></svg>SHRUB TRIMMING</li>
        <li><svg viewBox="0 0 14 14"><path d="M2 12 C2 5 6 2 13 2 C13 9 9 12 2 12 Z" fill="#a8d42f"/></svg>AERATION</li>
        <li><svg viewBox="0 0 14 14"><path d="M2 12 C2 5 6 2 13 2 C13 9 9 12 2 12 Z" fill="#a8d42f"/></svg>FLOWER BED MAINTENANCE</li>
        <li><svg viewBox="0 0 14 14"><path d="M2 12 C2 5 6 2 13 2 C13 9 9 12 2 12 Z" fill="#a8d42f"/></svg>FALL/SPRING CLEAN UP</li>
      </ul>
    </section>

    <div class="abs price-lawn">
      <div class="price-main">Lawn service<br>starting at <span class="price-fig">$40</span></div>
      <div class="price-note">(mowing, edging, leaf blowing)</div>
    </div>
    <div class="abs price-tree">Tree trimming<br>starting at <span class="price-fig">$125</span></div>

    <div class="abs footer-band"></div>
    <div class="abs coverage-pill">
      <div class="coverage-area">SERVING NEW BRAUNFELS AND SURROUNDING AREAS</div>
      <div class="coverage-type">RESIDENTIAL AND COMMERCIAL</div>
    </div>
    <div class="abs cta-label">TO SET UP AND ESTIMATE</div>
    <div class="abs cta-phone">Call : 512 555 0143</div>
    <div class="abs cta-email">or email <span class="email-address">mrpellowesyard@example-mail.net</span></div>
  </main>
</body>
</html>
```